Venturo Australia
Project: Venturo Australia - Stationary
Venturo Australia - Stationary - Travel
Venturo Australia - Stationary
Bright & Fun-filled
Giulia Rossabene
Director
17 Harlow Crescent, Bramwick Heights, Western Australia 6012
giulia@venturoaustralia.example
www.venturoaustralia.example

```html
<!DOCTYPE html>
<html lang="en">
<head>
<meta charset="utf-8">
<title>Venturo Australia – Stationery</title>
<link href="https://fonts.googleapis.com/css2?family=Oswald:wght@500;600&family=Montserrat:wght@400;600;700&display=swap" rel="stylesheet">
<style>
  :root{
    --bg:#ffffff;
    --paper:#ffffff;
    --blue:#1a8fd6;
    --blue-deep:#1576b4;
    --navy:#2b3a55;
    --orange:#f0782a;
    --green:#5ab947;
    --teal:#27a7c9;
    --grey:#5d6673;
    --rule:#e3e6ea;
  }
  *{margin:0;padding:0;box-sizing:border-box}
  html,body{width:1200px;height:802px;overflow:hidden;background:var(--bg)}
  body{position:relative;font-family:"Montserrat",sans-serif;color:var(--navy)}

  .stripe{position:absolute;left:0;right:0;bottom:0;height:8px;display:flex}
  .stripe span{flex:1}
  .stripe .s1{background:var(--blue)}
  .stripe .s2{background:var(--navy)}
  .stripe .s3{background:var(--orange)}
  .stripe .s4{background:var(--teal)}
  .stripe .s5{background:var(--green)}

  .wordmark{font-family:"Oswald",sans-serif;font-weight:600;color:var(--blue);line-height:1;display:flex;align-items:center;gap:8px}
  .wordmark .dot{width:14px;height:14px;border-radius:50%;background:var(--orange);flex:none}
  .tagline{font-family:"Montserrat",sans-serif;font-weight:700;font-size:8px;letter-spacing:1.5px;color:var(--green);margin-top:6px}

  /* business card front */
  .card-front{position:absolute;left:103px;top:199px;width:389px;height:173px;background:var(--paper);border-radius:6px;box-shadow:0 3px 10px rgba(0,0,0,.18);overflow:hidden}
  .card-front .brand{position:absolute;left:24px;top:46px}
  .card-front .wordmark{font-size:27px}
  .card-front .divider{position:absolute;left:238px;top:22px;width:1px;height:104px;background:var(--rule)}
  .card-front .contact{position:absolute;left:250px;top:22px;width:130px}
  .person-name{font-family:"Oswald",sans-serif;font-weight:600;font-size:13px;color:var(--orange);letter-spacing:.5px}
  .person-role{font-family:"Oswald",sans-serif;font-weight:500;font-size:7px;letter-spacing:3px;color:var(--navy);margin-bottom:8px}
  .contact-row{display:flex;align-items:flex-start;gap:5px;font-size:5.5px;line-height:1.35;color:var(--grey);margin-bottom:5px}
  .contact-row svg{flex:none;width:9px;height:9px}
  .card-front .url{position:absolute;left:0;right:0;bottom:20px;text-align:center;font-size:7px;letter-spacing:2.5px;color:var(--grey)}

  /* business card back */
  .card-back{position:absolute;left:103px;top:432px;width:401px;height:230px;border-radius:6px;background:radial-gradient(circle at 50% 45%,#3fb0e6 0%,var(--blue) 55%,var(--blue-deep) 100%);box-shadow:0 3px 10px rgba(0,0,0,.2);overflow:hidden}
  .card-back .wordmark{position:absolute;left:0;right:0;top:82px;justify-content:center;font-size:34px;color:#ffffff}
  .card-back .wordmark .dot{background:#ffffff}
  .card-back .url{position:absolute;left:0;right:0;bottom:28px;text-align:center;font-size:7px;letter-spacing:2.5px;color:rgba(255,255,255,.85)}

  /* letterhead */
  .letterhead{position:absolute;left:595px;top:43px;width:509px;height:706px;background:var(--paper);box-shadow:0 3px 14px rgba(0,0,0,.16);overflow:hidden}
  .letterhead .brand{position:absolute;right:48px;top:88px;text-align:right}
  .letterhead .wordmark{font-size:30px;justify-content:flex-end}
  .letterhead .tagline{font-size:8px}
  .recipient{position:absolute;left:40px;top:102px;width:150px}
  .recipient i,.body-lines i{display:block;height:1px;background:var(--rule)}
  .recipient i{margin-bottom:12px}
  .body-lines{position:absolute;left:40px;right:40px;top:222px}
  .body-lines i{margin-bottom:17px}
  .sign{position:absolute;left:40px;top:535px}
  .sign .person-name{color:var(--navy);font-size:14px}
  .sign .person-role{font-size:6px}
  .footer{position:absolute;left:0;right:0;top:633px;text-align:center;font-size:5.5px;line-height:1.5;color:var(--grey);font-weight:600}
</style>
</head>
<body>

  <section class="card-front" aria-label="Business card, front">
    <div class="brand">
      <div class="wordmark"><span class="dot"></span>Venturo Australia</div>
      <div class="tagline">STUDY | LIVE | TRAVEL</div>
    </div>
    <div class="divider"></div>
    <div class="contact">
      <div class="person-name">GIULIA ROSSABENE</div>
      <div class="person-role">DIRECTOR</div>
      <div class="contact-row">
        <svg viewBox="0 0 10 10"><circle cx="5" cy="5" r="5" fill="var(--orange)"/><path d="M5 2.2a2 2 0 0 0-2 2c0 1.5 2 3.6 2 3.6s2-2.1 2-3.6a2 2 0 0 0-2-2z" fill="#fff"/></svg>
        <span>17 Harlow Crescent, Bramwick Heights,<br>Western Australia 6012</span>
      </div>
      <div class="contact-row">
        <svg viewBox="0 0 10 10"><circle cx="5" cy="5" r="5" fill="var(--orange)"/><path d="M3.3 2.6l1 1-.5.7c.3.6.8 1.1 1.4 1.4l.7-.5 1 1-.6.8C4.8 6.8 3.2 5.2 2.5 3.2z" fill="#fff"/></svg>
        <span>+61 08 9412 5530</span>
      </div>
      <div class="contact-row">
        <svg viewBox="0 0 10 10"><circle cx="5" cy="5" r="5" fill="var(--orange)"/><rect x="3.4" y="2.2" width="3.2" height="5.6" rx=".6" fill="#fff"/></svg>
        <span>+61 0412 778 306</span>
      </div>
      <div class="contact-row">
        <svg viewBox="0 0 10 10"><circle cx="5" cy="5" r="5" fill="var(--orange)"/><rect x="2.5" y="3.2" width="5" height="3.6" fill="#fff"/><path d="M2.5 3.2L5 5.2l2.5-2" stroke="var(--orange)" stroke-width=".6" fill="none"/></svg>
        <span>giulia@venturoaustralia.example</span>
      </div>
    </div>
    <div class="url">www.venturoaustralia.example</div>
    <div class="stripe"><span class="s1"></span><span class="s2"></span><span class="s3"></span><span class="s4"></span><span class="s5"></span></div>
  </section>

  <section class="card-back" aria-label="Business card, back">
    <div class="wordmark"><span class="dot"></span>Venturo Australia</div>
    <div class="url">www.venturoaustralia.example</div>
  </section>

  <section class="letterhead" aria-label="Letterhead">
    <div class="brand">
      <div class="wordmark"><span class="dot"></span>Venturo Australia</div>
      <div class="tagline">STUDY | LIVE | TRAVEL</div>
    </div>
    <div class="recipient"><i></i><i></i><i></i><i></i></div>
    <div class="body-lines">
      <i></i><i></i><i></i><i></i><i></i><i></i><i></i><i></i><i></i><i></i><i></i><i></i><i></i><i></i><i></i>
    </div>
    <div class="sign">
      <div class="person-name">Giulia Rossabene</div>
      <div class="person-role">DIRECTOR</div>
    </div>
    <div class="footer">
      17 Harlow Crescent, Bramwick Heights,<br>
      Western Australia 6012<br>
      giulia@venturoaustralia.example<br>
      www.venturoaustralia.example
    </div>
    <div class="stripe"><span class="s1"></span><span class="s2"></span><span class="s3"></span><span class="s4"></span><span class="s5"></span><span class="s2"></span></div>
  </section>

</body>
</html>
```